Pricing Sheet for HVAC maintenance plan

I have a pricing sheet for our maintenance plan for my HVAC company. I want to have it put in a more appealing format than just a simple spreadsheet. I need it to be easy to read and yet exciting to look at.

Attached is the form in its word document. We need to have a signature line added as well.

Attached is also the company logo

Target Market(s)

Homeowners, both young and old

Industry/Entity Type

Hvac

Font styles to use
Serif

Colors
fbf289
ec1f27
faa54b
ffffff

Requirements
Must have
• Something that is easy to read.
• Must have logo
• Must have a signature and date line added
• Company colors - attached are some screenshots of what the color scheme might be. You can use this to draw inspiration
• Could be done on a dark background including black, as we paint our trucks black
Should not have
• Too much clutter.

```html
<!DOCTYPE html>
<html lang="en">
<head>
<meta charset="utf-8">
<title>Warmline Specialists – Maintenance Plan Pricing</title>
<link href="https://fonts.googleapis.com/css2?family=Lato:wght@400;700;900&display=swap" rel="stylesheet">
<style>
  :root {
    --yellow: #fbf289;
    --red: #ec1f27;
    --orange: #faa54b;
    --white: #ffffff;
    --black: #0a0a0a;
    --backdrop: #e4e4e4;
    --ink: #1c1c1c;
    --line-soft: #d8cd6a;
  }
  * { box-sizing: border-box; margin: 0; padding: 0; }
  html, body { width: 1200px; height: 752px; overflow: hidden; }
  body { background: var(--backdrop); font-family: "Lato", sans-serif; position: relative; }

  .sheet {
    position: absolute; left: 345px; top: 16px;
    width: 509px; height: 720px;
    background: var(--black);
    overflow: hidden;
  }
  .sheet-top { position: absolute; left: 0; top: 0; width: 509px; height: 140px; }
  .brand {
    position: absolute; top: 38px; left: 0; width: 100%;
    text-align: center; color: var(--red);
    font-weight: 900; font-size: 22px; letter-spacing: 1px;
  }

  .customer-form {
    position: absolute; left: 14px; top: 133px; width: 481px; height: 146px;
    background: var(--white); border: 2px solid var(--red); border-radius: 12px;
    padding: 3px 6px 0;
  }
  .form-field {
    height: 17px; line-height: 17px; font-size: 9.5px; font-weight: 700;
    color: var(--red); border-bottom: 1px solid var(--red);
  }
  .form-field:last-child { border-bottom: none; }

  .price-section { position: absolute; left: 16px; width: 476px; }
  .section-header {
    display: grid; grid-template-columns: 226px 111px 135px; column-gap: 2px;
    height: 21px; line-height: 21px; border-radius: 7px 7px 3px 3px;
    background: var(--orange); color: var(--ink);
    font-weight: 900; font-size: 11.5px;
  }
  .section-header span:first-child { padding-left: 18px; }
  .section-header span { text-align: center; }
  .section-header span:first-child { text-align: left; }
  .section-tab {
    width: 226px; height: 20px; line-height: 20px; padding-left: 18px;
    border-radius: 7px 7px 3px 3px; font-weight: 900; font-size: 11.5px;
  }
  .section-tab.red { background: var(--red); color: var(--white); }
  .section-tab.orange { background: var(--orange); color: var(--ink); }

  .price-row {
    display: grid; grid-template-columns: 226px 111px 135px; column-gap: 2px;
    height: 13.2px; line-height: 13px; font-size: 8.3px; color: var(--ink);
  }
  .price-row .item { background: var(--yellow); padding-left: 18px; border-bottom: 1px solid var(--line-soft); }
  .price-row .price {
    background: linear-gradient(#ffffff, #ececec);
    text-align: center; border-bottom: 1px solid var(--red);
  }
  .price-row:first-of-type .price { border-top: 1px solid var(--red); }
  .price-rows .price-row:last-child .item { border-bottom: none; border-bottom-left-radius: 6px; }
  .price-rows .price-row:last-child .price { border-bottom: none; }
  .price-rows .price-row:last-child .price:last-child { border-bottom-right-radius: 7px; }
  .price-rows { margin-top: 1px; }

  .signature-line {
    position: absolute; left: 16px; right: 16px; top: 647px;
    display: flex; justify-content: space-between;
    color: var(--yellow); font-size: 9.5px;
  }
  .credentials {
    position: absolute; left: 16px; right: 16px; top: 670px;
    display: flex; justify-content: space-between;
    color: var(--yellow); font-size: 9.5px; line-height: 13px;
  }
  .credentials .contact { text-align: right; }
</style>
</head>
<body>
  <main class="sheet">
    <svg class="sheet-top" viewBox="0 0 509 140" aria-hidden="true">
      <path d="M0 0 H509 V4 C430 58 330 110 254.5 112 C179 110 79 58 0 4 Z" fill="#ffffff"/>
      <path d="M0 4 C79 58 179 110 254.5 112 C330 110 430 58 509 4 V13 C430 68 330 120 254.5 121 C179 120 79 68 0 13 Z" fill="#ec1f27"/>
    </svg>
    <div class="brand">WARMLINE SPECIALISTS</div>

    <section class="customer-form">
      <div class="form-field">NAME:</div>
      <div class="form-field">ADDRESS:</div>
      <div class="form-field">CITY:</div>
      <div class="form-field">HOME PHONE:</div>
      <div class="form-field">CELL PHONE:</div>
      <div class="form-field">EMAIL ADDRESS:</div>
      <div class="form-field">CREDIT CARD NUMBER:</div>
      <div class="form-field">EXPIRATION DATE/CCV:</div>
    </section>

    <section class="price-section" style="top:281px">
      <div class="section-header"><span>COMBINATION PACKAGES</span><span>ASSURED PLAN</span><span>PREFERRED PLAN</span></div>
      <div class="price-rows">
        <div class="price-row"><span class="item">A/C and Electric Heat</span><span class="price">26.35</span><span class="price">47.45</span></div>
        <div class="price-row"><span class="item">A/C and Gas Furnace</span><span class="price">26.35</span><span class="price">47.45</span></div>
        <div class="price-row"><span class="item">A/C and Boiler</span><span class="price">35.00</span><span class="price">56.42</span></div>
        <div class="price-row"><span class="item">Heat Pump</span><span class="price">31.00</span><span class="price">60.42</span></div>
        <div class="price-row"><span class="item">A/C and Oil Boiler</span><span class="price">33.00</span><span class="price">65.42</span></div>
      </div>
    </section>

    <section class="price-section" style="top:370px">
      <div class="section-tab red">SEPARATE SYSTEMS</div>
      <div class="price-rows">
        <div class="price-row"><span class="item">A/C Only</span><span class="price">16.50</span><span class="price">31.32</span></div>
        <div class="price-row"><span class="item">Gas Furnace Only</span><span class="price">14.50</span><span class="price">24.12</span></div>
        <div class="price-row"><span class="item">Gas Boiler Only</span><span class="price">14.54</span><span class="price">35.33</span></div>
        <div class="price-row"><span class="item">Oil Boiler</span><span class="price">16.54</span><span class="price">39.33</span></div>
      </div>
    </section>

    <section class="price-section" style="top:444px">
      <div class="section-tab orange">OPTIONAL EQUIPMENT</div>
      <div class="price-rows">
        <div class="price-row"><span class="item">Humidifier</span><span class="price">6.50</span><span class="price">9.21</span></div>
        <div class="price-row"><span class="item">Electronic Air Cleaner</span><span class="price">5.00</span><span class="price">9.53</span></div>
        <div class="price-row"><span class="item">Media Air Cleaner</span><span class="price">5.65</span><span class="price">12.50</span></div>
        <div class="price-row"><span class="item">Attic Ventilation Fan</span><span class="price">9.54</span><span class="price">12.45</span></div>
        <div class="price-row"><span class="item">Dehumidifier</span><span class="price">7.12</span><span class="price">12.09</span></div>
      </div>
    </section>

    <section class="price-section" style="top:534px">
      <div class="section-tab red">ELECTRIC PLAN</div>
      <div class="price-rows">
        <div class="price-row"><span class="item">Interior Electric</span><span class="price"></span><span class="price">15.23</span></div>
        <div class="price-row"><span class="item">Generator Maintenance Plan</span><span class="price"></span><span class="price">34.12</span></div>
        <div class="price-row"><span class="item">Prices are per month, per system</span><span class="price"></span><span class="price"></span></div>
      </div>
    </section>

    <div class="signature-line">
      <span>Signature:____________________</span>
      <span>Date:____________________</span>
    </div>

    <footer class="credentials">
      <div class="licenses">
        NJ Electrical License #20415<br>
        NJ Home Improvement Business Registration # 14VH0218834<br>
        NJ HVAC Lic # 582
      </div>
      <div class="contact">
        www.WarmlineSpecialistsLLC.com<br>
        Info@WarmlineSpecialistsLLC.com<br>
        P.O.Box 412 Maple Run, NJ, 07811
      </div>
    </footer>
  </main>
</body>
</html>
```